Meridian Sound Wellness LLC Card Design

Need business card with a logo for a hearing aid sales and audiology business. We have two Hearing Instrument Specialists and one Audiologist on staff. Over 25 years in business. Locally owned and operated. Financing available. Most insurances accepted.

Meridian Sound Wellness LLC
48730 W Linden Row, Suite 9
Spokane, WA 99481
509-617-2085
www.meridiansoundnorth.example

Manager
Tobias Wrenfield HIS COHC
License #81729046

Target Market(s)

50yr old + people with a hearing loss.

Industry/Entity Type

Business

Contact Information for Business Card

48730 W Linden Row, Suite 9
Spokane, WA 99481
509-617-2085
www.meridiansoundnorth.example

Manager
Tobias Wrenfield HIS COHC
NRPL #81729046

Font styles to use
Serif
Sans Serif

Requirements
Must have
• Business name, Tobias's name and title(s) and contact information, License #, web address
Nice to have
Should not have

```html
<!DOCTYPE html>
<html lang="en">
<head>
<meta charset="utf-8">
<title>Meridian Sound Wellness LLC – Business Card</title>
<link href="https://fonts.googleapis.com/css2?family=Raleway:wght@400;500&family=Arimo:wght@400&display=swap" rel="stylesheet">
<style>
  :root {
    --sky: #00aeef;
    --leaf: #2bb673;
    --paper: #ffffff;
  }
  html, body {
    margin: 0;
    padding: 0;
    overflow: hidden;
    background: var(--paper);
  }
  .card {
    position: relative;
    width: 1200px;
    height: 800px;
    background: var(--paper);
    overflow: hidden;
    font-family: "Raleway", sans-serif;
  }
  .block { position: absolute; }
  .block--sky-corner { left: 0; top: 0; width: 110px; height: 200px; background: var(--sky); }
  .block--sky-stripe { left: 78px; top: 0; width: 32px; height: 424px; background: var(--sky); }
  .block--leaf-top { left: 110px; top: 0; width: 260px; height: 110px; background: var(--leaf); }
  .block--leaf-side { left: 1090px; top: 472px; width: 110px; height: 218px; background: var(--leaf); }
  .block--sky-foot { left: 906px; top: 690px; width: 294px; height: 110px; background: var(--sky); }

  .rule { position: absolute; background: var(--sky); }
  .rule--brand { left: 110px; top: 200px; width: 742px; height: 3px; }
  .rule--person { left: 110px; top: 374px; width: 414px; height: 3px; }
  .rule--contact { left: 574px; top: 470px; width: 626px; height: 5px; }

  .brand-name {
    position: absolute;
    left: 124px;
    top: 138px;
    margin: 0;
    font-family: "Raleway", sans-serif;
    font-weight: 400;
    font-size: 46px;
    line-height: 56px;
    letter-spacing: 0.5px;
    color: var(--leaf);
    white-space: nowrap;
  }

  .person {
    position: absolute;
    left: 124px;
    top: 286px;
    margin: 0;
    color: var(--sky);
    white-space: nowrap;
  }
  .person__name {
    display: block;
    font-weight: 500;
    font-size: 34px;
    line-height: 40px;
  }
  .person__title {
    display: block;
    font-weight: 400;
    font-size: 34px;
    line-height: 40px;
  }
  .license {
    position: absolute;
    left: 122px;
    top: 390px;
    margin: 0;
    font-family: "Arimo", sans-serif;
    font-size: 25px;
    line-height: 32px;
    color: var(--leaf);
    white-space: nowrap;
  }

  .contact {
    position: absolute;
    left: 574px;
    top: 490px;
    margin: 0;
    padding: 0;
    list-style: none;
    font-family: "Arimo", sans-serif;
    font-size: 29px;
    line-height: 34px;
    letter-spacing: -0.2px;
    color: var(--sky);
    white-space: nowrap;
  }
  .contact__item {
    position: relative;
    padding-left: 66px;
  }
  .contact__item--address { height: 82px; }
  .contact__item--phone { height: 54px; }
  .contact__icon {
    position: absolute;
    left: 0;
    fill: var(--leaf);
  }
</style>
</head>
<body>
  <div class="card">
    <div class="block block--sky-corner"></div>
    <div class="block block--sky-stripe"></div>
    <div class="block block--leaf-top"></div>

    <h1 class="brand-name">Meridian Sound Wellness LLC</h1>
    <div class="rule rule--brand"></div>

    <p class="person">
      <span class="person__name">Tobias Wrenfield HIS COHC</span>
      <span class="person__title">Manager</span>
    </p>
    <div class="rule rule--person"></div>
    <p class="license">NRPL # 81729046</p>

    <div class="rule rule--contact"></div>
    <div class="block block--leaf-side"></div>
    <div class="block block--sky-foot"></div>

    <ul class="contact">
      <li class="contact__item contact__item--address">
        <svg class="contact__icon" style="top:2px" width="48" height="40" viewBox="0 0 50 42" aria-hidden="true">
          <path d="M25 2 L2 22 H9 V40 H20 V28 H30 V40 H41 V22 H48 Z"/>
        </svg>
        48730 W Linden Row, Suite 9<br>Spokane, WA 99481
      </li>
      <li class="contact__item contact__item--phone">
        <svg class="contact__icon" style="left:8px;top:0" width="32" height="34" viewBox="0 0 32 34" aria-hidden="true">
          <path d="M7 1 C4 1 1 4 1 8 C2 20 13 32 26 33 C30 33 31 30 31 28 L31 24 L23 20 L19 24 C14 22 11 18 9 13 L13 9 L10 1 Z"/>
        </svg>
        509-617-2085
      </li>
      <li class="contact__item">
        <svg class="contact__icon" style="left:4px;top:-2px" width="38" height="38" viewBox="0 0 40 40" aria-hidden="true">
          <circle cx="20" cy="20" r="19"/>
          <g fill="none" stroke="#ffffff" stroke-width="2.5">
            <ellipse cx="20" cy="20" rx="8" ry="17"/>
            <line x1="3" y1="20" x2="37" y2="20"/>
            <line x1="20" y1="3" x2="20" y2="37"/>
          </g>
        </svg>
        www.meridiansoundnorth.example
      </li>
    </ul>
  </div>
</body>
</html>
```